Site for a workout and Consulting enterprise

I need a professional responsive site for www.valomer.hamburg. The website shoulderstand consist of a Landing and 4 other pages. - On page for the contact informations - on page for the about - on page for consulting services (technical) - on page for Training and workshop services (business and soft skills) I add some files so you can see my idea of the design.
Target Market(s)
IT and Management
Industry/Entity Type
Management Consulting
Coding
Coded - Design and coding required
Number of Pages Required
4 page
Requirements
Must have
- Use Pictures for Background, Sliders and Topics. Just have to placeholders for the design.

```html
<!DOCTYPE html>
<html lang="en">
<head>
<meta charset="utf-8">
<title>Contact Us – valomer</title>
<link rel="stylesheet" href="https://fonts.googleapis.com/css2?family=Raleway:ital,wght@0,400;0,500;0,700;1,400&family=Ubuntu:wght@400&display=swap">
<style>
  :root {
    --navy: #06325a;
    --teal: #1abc9c;
    --field-border: #a9a9a9;
    --placeholder: #a8a8a8;
    --success-bg: #dff0d8;
    --success-border: #d0e9c6;
    --success-text: #3c763d;
    --rule: #8fb0c4;
    --white: #ffffff;
  }
  * { box-sizing: border-box; margin: 0; padding: 0; }
  html, body { width: 1200px; height: 919px; overflow: hidden; background: var(--white); font-family: "Raleway", sans-serif; }
  .page { position: relative; width: 1200px; height: 919px; }

  .site-header { position: absolute; left: 0; top: 0; width: 1200px; height: 84px; }
  .brand { position: absolute; left: 80px; top: 20px; display: flex; align-items: center; gap: 8px; font-family: "Raleway", sans-serif; font-weight: 500; font-size: 34px; color: var(--navy); line-height: 1; }
  .brand-mark { width: 26px; height: 26px; background: var(--navy); }

  .hero { position: absolute; left: 0; top: 84px; width: 1200px; height: 186px;
    background: linear-gradient(100deg, #3a3633 0%, #6b6560 35%, #a49d95 60%, #8a837c 100%); }
  .hero-title { position: absolute; left: 0; top: 84px; width: 1200px; height: 186px; display: flex; align-items: center; justify-content: center;
    font-family: "Ubuntu", sans-serif; font-size: 45px; color: var(--white); }

  .contact-form { position: absolute; left: 97px; top: 319px; width: 455px; }
  .alert-success { position: absolute; left: 0; top: 0; width: 399px; height: 47px; background: var(--success-bg); border: 1px solid var(--success-border);
    color: var(--success-text); font-size: 17px; font-family: Arial, sans-serif; display: flex; align-items: center; padding-left: 15px; gap: 6px; }
  .alert-close { position: absolute; right: 14px; top: 14px; color: #9aa89a; font-size: 16px; }
  .field { position: absolute; left: 3px; width: 450px; height: 36px; border: 2px solid var(--field-border); border-radius: 3px;
    font-size: 17px; color: var(--placeholder); padding: 7px 10px; text-transform: uppercase; }
  .field--name { top: 67px; }
  .field--email { top: 124px; }
  .field--phone { top: 180px; }
  .field--message { top: 236px; height: 85px; }
  .terms { position: absolute; left: 4px; top: 335px; display: flex; align-items: center; gap: 8px; font-size: 13.5px; color: var(--placeholder); }
  .terms-box { width: 16px; height: 16px; border-radius: 3px; background: var(--teal); display: flex; align-items: center; justify-content: center; }
  .btn-send { position: absolute; left: 385px; top: 363px; width: 69px; height: 24px; border-radius: 3px; background: var(--teal); color: var(--white);
    font-weight: 700; font-size: 13px; display: flex; align-items: center; justify-content: center; }

  .map { position: absolute; left: 600px; top: 316px; width: 600px; height: 354px; background: linear-gradient(135deg, #e6dfcf 0%, #e9e6df 50%, #dfd9c8 100%); }
  .contact-panel { position: absolute; left: 600px; top: 670px; width: 600px; height: 111px; background: var(--navy); color: var(--white); }
  .contact-item { position: absolute; top: 40px; }
  .contact-item--email { left: 26px; }
  .contact-item--address { left: 354px; }
  .contact-label { font-weight: 700; font-size: 13.5px; letter-spacing: -0.2px; }
  .contact-value { font-style: italic; font-size: 13.5px; margin-top: 5px; letter-spacing: -0.3px; }

  .footer-rule { position: absolute; left: 0; top: 804px; width: 1200px; height: 1px; background: var(--rule); }
  .btn-back { position: absolute; left: 1023px; top: 829px; width: 111px; height: 32px; border-radius: 3px; background: var(--navy); color: var(--white);
    font-size: 14px; display: flex; align-items: center; justify-content: center; }
</style>
</head>
<body>
<div class="page">
  <header class="site-header">
    <div class="brand"><span class="brand-mark"></span>valomer</div>
  </header>

  <div class="hero" role="img" aria-label="Photo of a keyboard, notebook and pen in sepia tones"></div>
  <h1 class="hero-title">Contact Us</h1>

  <form class="contact-form">
    <div class="alert-success">
      <svg width="16" height="16" viewBox="0 0 16 16"><path d="M2 9 L6 13 L14 2" fill="none" stroke="#3c763d" stroke-width="1.3"/></svg>
      Success!
      <span class="alert-close">×</span>
    </div>
    <div class="field field--name">Name</div>
    <div class="field field--email">Email</div>
    <div class="field field--phone">Phone</div>
    <div class="field field--message">Message</div>
    <div class="terms">
      <span class="terms-box"><svg width="10" height="10" viewBox="0 0 10 10"><path d="M1.5 5 L4 7.5 L8.5 2.5" fill="none" stroke="#fff" stroke-width="1.8"/></svg></span>
      I read and accept the terms and conditions
    </div>
    <div class="btn-send">SEND</div>
  </form>

  <div class="map" role="img" aria-label="Street map showing the office location with a red pin"></div>
  <section class="contact-panel">
    <div class="contact-item contact-item--email">
      <div class="contact-label">CONTACT EMAIL</div>
      <div class="contact-value">hello@valomer-mail.de</div>
    </div>
    <div class="contact-item contact-item--address">
      <div class="contact-label">CONTACT ADDRESS</div>
      <div class="contact-value">your address there</div>
    </div>
  </section>

  <div class="footer-rule"></div>
  <div class="btn-back">&lt; Back</div>
</div>
</body>
</html>
```